Company letter head and business card for new Indian Pharmaceutical Export company.

We need a letterhead and business card design for an Indian Pharmaceutical Export company.

The letter head needs to contain the following information.
Vorin Healthline Pvt. Ltd.
Office No 4827 Plot No 19, Larkspire, KT Lane, 400153, Maharashtra, India.
Email: info@vorin-healthline.com
Phone: +91-8342196507
CIN: U71853MH2025PTC902617
GSTIN: (This number is still pending, we will add later)

The business card needs to contain:
Address:
Vorin Healthline Pvt. Ltd.
Office No 4827 Plot No19, Larkspire, KT Lane, 400153, MH, India.
Email: torvald@vorin-healthline.com
Phone: +49-17634902851
Name on card: Torvald Ramming
Position: Director

The design for the letter head and business card should be simple but trustworthy.
Please use only Green and blue, same as in the attached logo.

```html
<!DOCTYPE html>
<html lang="en">
<head>
<meta charset="utf-8">
<title>Vorin Healthline Letterhead</title>
<link rel="stylesheet" href="https://fonts.googleapis.com/css2?family=Arimo:wght@400;700&family=Montserrat:wght@700&display=swap">
<style>
  :root {
    --brand-blue: #1a66b8;
    --brand-green: #7dba3e;
    --ink: #4a4a4a;
    --rule: #555555;
    --paper: #f6f6f7;
    --backdrop: #cbcdcd;
  }
  * { margin: 0; padding: 0; box-sizing: border-box; }
  html, body { width: 1073px; height: 1200px; overflow: hidden; }
  body {
    background: var(--backdrop);
    font-family: "Arimo", Arial, sans-serif;
    color: var(--ink);
    position: relative;
  }
  .letterhead {
    position: absolute;
    left: 130px; top: 20px;
    width: 813px; height: 1160px;
    background: linear-gradient(180deg, #f8f8f9 0%, var(--paper) 60%, #eeeef0 100%);
    box-shadow: 0 6px 24px rgba(0,0,0,0.18);
  }
  .brand {
    position: absolute;
    left: 40px; top: 96px;
    display: flex; align-items: center; gap: 8px;
  }
  .brand-dot {
    width: 14px; height: 14px; border-radius: 50%;
    background: var(--brand-green);
  }
  .brand-name {
    font-family: "Montserrat", Arial, sans-serif;
    font-weight: 700; font-size: 15px;
    color: var(--brand-blue);
    white-space: nowrap;
  }
  .divider {
    position: absolute; top: 66px;
    width: 1.5px; height: 85px;
    background: var(--rule);
  }
  .divider--first { left: 228px; }
  .divider--second { left: 508px; }
  .address {
    position: absolute; left: 283px; top: 75px;
    font-size: 13px; line-height: 16.7px;
  }
  .company-name { color: var(--brand-blue); font-weight: 700; }
  .contact {
    position: absolute; left: 554px; top: 74px;
    font-size: 13px; line-height: 16.7px;
  }
  .contact-line { display: flex; align-items: center; gap: 4px; white-space: nowrap; }
  .contact-line svg { width: 11px; height: 11px; fill: var(--brand-green); }
  .label { color: var(--brand-green); font-weight: 700; }
  .letter {
    position: absolute; left: 73px; top: 358px;
    width: 666px;
  }
  .salutation { font-size: 18.5px; margin-bottom: 28px; margin-left: 1px; }
  .letter p.body {
    font-size: 13.6px; line-height: 16.8px;
    margin-bottom: 14.8px;
  }
  .closing { font-size: 11px; margin-top: 22px; margin-left: 1px; }
  .signature {
    margin-top: 22px; margin-left: 1px;
    width: 100px; height: 30px;
    background: linear-gradient(90deg, rgba(60,60,60,0.18), rgba(60,60,60,0.08));
    border-radius: 3px;
  }
</style>
</head>
<body>
  <main class="letterhead">
    <header>
      <div class="brand">
        <span class="brand-dot"></span>
        <span class="brand-name">Vorin Healthline</span>
      </div>
      <span class="divider divider--first"></span>
      <address class="address" style="font-style:normal">
        <div class="company-name">Vorin Healthline Pvt. Ltd.</div>
        <div>Office No 4827 Plot No 19</div>
        <div>Larkspire, KT Lane</div>
        <div>400153, Maharashtra, India.</div>
      </address>
      <span class="divider divider--second"></span>
      <div class="contact">
        <div class="contact-line">
          <svg viewBox="0 0 24 24"><path d="M2 9c0-3 4-5 10-5s10 2 10 5v2h-5V9c-1-1-3-1.5-5-1.5S8 8 7 9v2H2z M6 12h12l2 8H4z"/></svg>
          <span>+91-8342196507</span>
        </div>
        <div class="contact-line">
          <svg viewBox="0 0 24 24"><path d="M2 9l10-7 10 7v13H2z M5 10l7 5 7-5v-1l-7 4-7-4z"/></svg>
          <span>info@vorin-healthline.com</span>
        </div>
        <div class="contact-line"><span class="label">CIN:</span> <span>U71853MH2025PTC902617</span></div>
        <div class="contact-line"><span class="label">GSTIN:</span> <span>0027481936502718</span></div>
      </div>
    </header>

    <section class="letter">
      <p class="salutation">Dear Mr. Smith,</p>
      <p class="body">Lorem ipsum dolor sit amet, consectetuer adipiscing elit, sed diam nonmmy nibh euismod tincidunt ut laor eet dolore magna aliquam erat volutpat. Ut wisi enim ad minim veniam, quis nostrud exerci tationmcorper suscipit lobortis nisl ut aliquip ex ea commodo consequat. Duis autem vel eum iriure dolor in hendrerit in vulputate velit esse molestie consequat, vel illum dolore eu feugiat</p>
      <p class="body">Rorem ipsum dolor sit amet, consectetuer adipiscing elit, sed diam nonmmy nibh euismod tincidunt ut laor eet dolore magna aliquam erat volutpat. Ut wisi enim ad minim veniam, quis nostrud exerci tationmcorper suscipit lobortis nisl ut aliquip ex ea commodo consequat. Duis autem vel eum iriure dolor in hendrerit in vulputate velit esse molest</p>
      <p class="body">Dorem ipsum dolor sit amet, consectetuer adipiscing elit, sed diam nonmmy nibh euismod tincidunt ut laor eet dolore magna aliquam erat volutpat. Ut wisi enim ad minim veniam, quis nostrud exerci tationmcorper suscipit lobortis nisl ut aliquip ex ea commodo consequat. Duis autem vel eum iriure dolor in hendrerit in suscipit lobortis nisl ut aliquip ex ea commodo consequat. Duis autem vel eum iriure dolor in hendrerit in vulputate velit esse molestie consequat, vel illum</p>
      <p class="body">Sorem ipsum dolor sit amet, consectetuer adipiscing elit, sed diam nonmmy nibh euismod tincidunt ut laor eet dolore magna aliquam erat volutpat. Ut wisi enim ad minim veniam, quis nostrud exerci tationmcorper suscipit lobortis nisl ut aliquip ex ea commodo consequat. Duis autem vel eum iriure dolor in</p>
      <p class="closing">Sincerely,</p>
      <div class="signature" role="img" aria-label="Handwritten signature of the sender"></div>
    </section>
  </main>
</body>
</html>
```